Business Card Design Project

Business Card design based on logo.

I need business card, letterhead, envelope, and if possible, Powerpoint slide template.

On front of business card: Just logo- and  my name and title:  Helena Marsk, Principal

On reverse-logo and the rest of the contact info:

4871 Orchard Lane
Alder Springs, CA 95720
650-318-2274
hm@brevicaeducation.example

On letterhead-Just logo at top, at bottom  the rest-very small along the bottom

On PPT slide-just the logo.

I also want to try a few other colors-I like lime/dark grey (not black) but would like to try Sienna, maybe also indigo or bright blue-green.

I forgot to add-

On the business card-switch to vertical on reverse side and put:

Reverse side-switch to vertical and list:

Helena Marsk
Principal
Brevica Tutoring Partners, LLC

650-318-2274

4871 Orchard Lane
Alder Springs, CA 95720

Helena Marsk
Principal

650-318-2274

4871 Orchard Lane
Alder Springs, CA 95720

I have another project at the same time-for Stationery. Feel free to submit to that one also.

That one includes letterhead, envelope, PPT slide, folder cover sheet-HM

Industry/Entity Type

Business

Requirements
Must have
• Must use logo-preferably lime green version-with gray, not black or just 2-tone -logo on colored background.

```html
<!DOCTYPE html>
<html lang="en">
<head>
<meta charset="utf-8">
<title>Brevica Tutoring Stationery</title>
<link href="https://fonts.googleapis.com/css2?family=PT+Sans:wght@400;700&display=swap" rel="stylesheet">
<style>
  :root {
    --lime: #8aac2f;
    --lime-dark: #7a9c24;
    --ink: #2b2b2b;
    --grey: #5a5a5a;
    --paper: #f7f7f6;
    --backdrop: #e9e9e8;
    --rule: #cfcfcf;
    --window: #ebebeb;
  }
  * { box-sizing: border-box; margin: 0; padding: 0; }
  html, body { width: 1200px; height: 750px; overflow: hidden; }
  body {
    background: var(--backdrop);
    font-family: "PT Sans", sans-serif;
    color: var(--ink);
    position: relative;
  }
  .sheet { position: absolute; background: var(--paper); }

  /* wordmark */
  .wordmark { display: flex; align-items: center; gap: 6px; }
  .wordmark-square { background: var(--lime); flex: none; }
  .wordmark-name {
    font-family: "PT Sans", sans-serif; font-weight: 700;
    color: var(--grey); letter-spacing: 0.12em; text-transform: uppercase;
    line-height: 1.05;
  }
  .wordmark.light .wordmark-square { background: #fff; }
  .wordmark.light .wordmark-name { color: #fff; }

  /* letterhead */
  .letterhead { left: 114px; top: 38px; width: 456px; height: 648px; }
  .letterhead .wordmark { position: absolute; top: 72px; left: 0; right: 0; justify-content: center; }
  .letterhead .wordmark-square { width: 16px; height: 16px; }
  .letterhead .wordmark-name { font-size: 18px; text-align: center; }
  .letter { position: absolute; left: 63px; top: 177px; width: 336px; font-size: 9.2px; line-height: 1.26; }
  .letter p { margin-bottom: 16px; }
  .letter .body p { margin-bottom: 0; }
  .letter .closing { margin-top: 50px; }
  .signature-area { width: 60px; height: 22px; margin-top: 14px; background: linear-gradient(90deg, #e6e6ee, #eeeef3); border-radius: 3px; }
  .letter-footer {
    position: absolute; left: 0; right: 0; bottom: 24px;
    display: flex; justify-content: center; align-items: center; gap: 6px;
    font-size: 5.6px; color: var(--grey); white-space: nowrap;
  }
  .letter-footer .item { display: inline-flex; align-items: center; gap: 2px; }
  .icon { width: 6px; height: 6px; flex: none; }

  /* envelopes */
  .envelope-back { left: 611px; top: 39px; width: 513px; height: 244px; overflow: hidden; }
  .envelope-flap {
    position: absolute; left: 0; top: 0; width: 100%; height: 86px;
    background: var(--lime); border-radius: 0 0 8px 8px;
    display: flex; justify-content: center; align-items: center;
  }
  .envelope-flap .wordmark-square { width: 10px; height: 10px; }
  .envelope-flap .wordmark-name { font-size: 12px; }

  .envelope-front { left: 611px; top: 303px; width: 513px; height: 246px; }
  .envelope-front .wordmark { position: absolute; left: 24px; top: 36px; }
  .envelope-front .wordmark-square { width: 14px; height: 14px; }
  .envelope-front .wordmark-name { font-size: 15px; }
  .return-address { position: absolute; left: 24px; top: 108px; font-size: 6.4px; line-height: 1.4; color: var(--grey); }
  .address-window {
    position: absolute; left: 22px; top: 169px; width: 180px; height: 55px;
    background: var(--window); border: 1px solid #d8d8d8; border-radius: 6px;
  }

  /* business cards */
  .card-front { left: 612px; top: 569px; width: 206px; height: 117px; }
  .card-front .wordmark { position: absolute; left: 12px; top: 22px; }
  .card-front .wordmark-square { width: 8px; height: 8px; }
  .card-front .wordmark-name { font-size: 8.5px; }
  .card-person { position: absolute; right: 12px; top: 60px; text-align: right; line-height: 1.2; }
  .card-person .name { font-size: 6px; font-weight: 700; color: var(--lime); }
  .card-person .title { font-size: 4.8px; color: var(--grey); }
  .card-rule { position: absolute; left: 12px; right: 12px; top: 76px; height: 1px; background: var(--rule); }
  .card-contact { position: absolute; left: 12px; top: 82px; display: flex; gap: 14px; font-size: 4.6px; line-height: 1.55; color: var(--grey); }
  .card-contact .row { display: flex; align-items: center; gap: 2px; }
  .card-contact .icon { width: 4.5px; height: 4.5px; }

  .card-back { left: 842px; top: 569px; width: 205px; height: 117px; background: var(--lime-dark); display: flex; justify-content: center; align-items: center; }
  .card-back .wordmark-square { width: 8px; height: 8px; }
  .card-back .wordmark-name { font-size: 9px; }
</style>
</head>
<body>

<section class="sheet letterhead">
  <div class="wordmark">
    <span class="wordmark-square"></span>
    <span class="wordmark-name">Brevica<br>Tutoring</span>
  </div>
  <div class="letter">
    <p>Your Street Address<br>Your City, State&nbsp; Zip<br>Date</p>
    <p>First and Last Name of the Person to whom you are writing<br>Their Street Address<br>City, ST Zip</p>
    <p>Dear Mr./Ms. Full Name:</p>
    <div class="body">
      <p>You do not want to indent when you are using this format. This is the best format to use when you are writing a persuasive letter. You want to introduce yourself and the topic you are writing about to the reader. Remember that the first rule of writing is to know your audience. In a persuasive letter, you state your opinion or your feelings about something that is important to you after you have introduced yourself. You must sound as professional and passionate as possible. You do not want to belittle the reader or they will not finish reading your letter. Your letter needs to have the facts, reasons, and examples to support your position. Address issues that your reader may have in their argument.</p>
      <p>In a second paragraph, you must have solutions. Without solutions, you are only complaining. Offer assistance in solving the problem. Remind the reader where they can contact you.</p>
    </div>
    <p class="closing">Sincerely yours,</p>
    <div class="signature-area" role="img" aria-label="Handwritten signature"></div>
  </div>
  <footer class="letter-footer">
    <span>Brevica Tutoring Partners, LLC: 4871 Orchard Lane, Alder Springs, CA 95720</span>
    <span class="item">
      <svg class="icon" viewBox="0 0 10 10"><path d="M2 1h2l1 2.5-1.3 1a6 6 0 0 0 2.8 2.8l1-1.3L10 7v2a1 1 0 0 1-1 1A9 9 0 0 1 0 1a1 1 0 0 1 1-1z" fill="var(--lime)"/></svg>650-318-2274
    </span>
    <span class="item">
      <svg class="icon" viewBox="0 0 10 10"><circle cx="5" cy="5" r="5" fill="var(--lime)"/><rect x="2.3" y="3.2" width="5.4" height="3.6" fill="#fff"/></svg>hm@brevicaeducation.example
    </span>
    <span class="item">
      <svg class="icon" viewBox="0 0 10 10"><circle cx="5" cy="5" r="4.3" fill="none" stroke="var(--lime)" stroke-width="1.4"/><path d="M1 5h8M5 1v8" stroke="var(--lime)" stroke-width="0.9"/></svg>www.brevicaeducation.example
    </span>
  </footer>
</section>

<section class="sheet envelope-back">
  <div class="envelope-flap">
    <div class="wordmark light">
      <span class="wordmark-square"></span>
      <span class="wordmark-name">Brevica Tutoring</span>
    </div>
  </div>
</section>

<section class="sheet envelope-front">
  <div class="wordmark">
    <span class="wordmark-square"></span>
    <span class="wordmark-name">Brevica<br>Tutoring</span>
  </div>
  <p class="return-address">Brevica Tutoring Partners, LLC<br>4871 Orchard Lane, Alder Springs, CA 95720</p>
  <div class="address-window"></div>
</section>

<section class="sheet card-front">
  <div class="wordmark">
    <span class="wordmark-square"></span>
    <span class="wordmark-name">Brevica<br>Tutoring</span>
  </div>
  <div class="card-person">
    <div class="name">Helena Marsk</div>
    <div class="title">Principal</div>
  </div>
  <div class="card-rule"></div>
  <div class="card-contact">
    <div>Brevica Tutoring Partners, LLC<br>4871 Orchard Lane<br>Alder Springs, CA 95720</div>
    <div>
      <div class="row"><svg class="icon" viewBox="0 0 10 10"><circle cx="5" cy="5" r="5" fill="var(--lime)"/></svg>650-318-2274</div>
      <div class="row"><svg class="icon" viewBox="0 0 10 10"><circle cx="5" cy="5" r="5" fill="var(--lime)"/></svg>hm@brevicaeducation.example</div>
      <div class="row"><svg class="icon" viewBox="0 0 10 10"><circle cx="5" cy="5" r="5" fill="var(--lime)"/></svg>www.brevicaeducation.example</div>
    </div>
  </div>
</section>

<section class="sheet card-back">
  <div class="wordmark light">
    <span class="wordmark-square"></span>
    <span class="wordmark-name">Brevica<br>Tutoring</span>
  </div>
</section>

</body>
</html>
```